Brinevale Yacht Management Full Page Ad Flyer

Yacht Management Package also includes the following periodic Monthly services:

Monthly full vessel systems checklist inspections
Diver For Hull Cleaning And Inspection Of Props, Shafts, and Zincs
Interior/Exterior Detailing and scheduled washdowns
Manage Haulout
Pump-out Services
On-call Captain and Crew Services
Updates

Need more time to provide more content to designers and the printing press template file.

Target Market(s)

Vessel owners, motor yachts, sailboats from 25 feet in length up to 125 feet in length. We do not do cruise ships or yachts larger than 125 feet. Someone who has their boat docked at their house or a local marina. We also offer mobile on-site services.

```html
<!DOCTYPE html>
<html lang="en">
<head>
<meta charset="utf-8">
<title>Brinevale Yacht Management – Periodic Services Flyer</title>
<link rel="stylesheet" href="https://fonts.googleapis.com/css2?family=Barlow+Condensed:wght@600;700&family=Montserrat:wght@400;500&display=swap">
<style>
  :root {
    --paper: #f4f4f4;
    --ink: #111111;
    --navy: #1c3f86;
    --blue: #1d7dd0;
    --blue-deep: #0f6cc0;
    --sky-top: #6fb4ea;
    --sea: #1d5fb0;
    --white: #ffffff;
  }
  * { margin: 0; padding: 0; box-sizing: border-box; }
  html, body { width: 1200px; height: 1200px; overflow: hidden; background: var(--paper); }
  .flyer { position: relative; width: 1200px; height: 1200px; background: var(--paper); overflow: hidden; }
  .backdrop { position: absolute; inset: 0; width: 1200px; height: 1200px; }

  .brand { position: absolute; left: 70px; top: 170px; width: 450px; font-family: "Barlow Condensed", sans-serif; font-weight: 700; color: var(--navy); text-align: center; text-transform: uppercase; }
  .brand-name { display: block; font-size: 104px; line-height: 0.95; letter-spacing: 3px; }
  .brand-tagline { display: block; font-size: 33px; line-height: 1.3; letter-spacing: 6px; border-top: 4px solid var(--navy); margin-top: 6px; padding-top: 2px; }

  .headline { position: absolute; left: 70px; top: 362px; font-family: "Barlow Condensed", sans-serif; font-weight: 700; color: var(--ink); text-transform: uppercase; line-height: 1.0; }
  .headline-lead { display: block; font-size: 56px; letter-spacing: 0.5px; }
  .headline-line { display: block; font-size: 49px; letter-spacing: 0.5px; }
  .headline-underline { text-decoration: underline; text-decoration-thickness: 3px; text-underline-offset: 6px; }

  .services { position: absolute; left: 68px; top: 587px; list-style: none; font-family: "Montserrat", sans-serif; font-weight: 500; font-size: 29px; line-height: 35px; color: var(--ink); text-transform: uppercase; }
  .service { position: relative; padding-left: 71px; margin-bottom: 12px; }
  .service::before { content: ""; position: absolute; left: 0; top: 2px; width: 30px; height: 30px; border-radius: 50%; background: var(--blue); border: 3px solid var(--ink); }
  .service.single { margin-bottom: 17px; }

  .website { position: absolute; left: 71px; top: 1088px; font-family: "Montserrat", sans-serif; font-weight: 400; font-size: 28px; color: var(--ink); }

  .contact { position: absolute; left: 832px; top: 1038px; width: 320px; font-family: "Montserrat", sans-serif; color: var(--white); }
  .contact-call { display: flex; align-items: center; gap: 12px; margin-left: 52px; font-size: 25px; font-weight: 400; text-transform: uppercase; }
  .contact-call svg { width: 32px; height: 32px; }
  .contact-phone { display: block; margin-top: 10px; font-size: 37px; font-weight: 400; letter-spacing: 0.5px; }
</style>
</head>
<body>
<main class="flyer">
  <svg class="backdrop" viewBox="0 0 1024 1024" preserveAspectRatio="none">
    <defs>
      <linearGradient id="seaPhoto" x1="0" y1="0" x2="0" y2="1">
        <stop offset="0" stop-color="var(--sky-top)"/>
        <stop offset="0.45" stop-color="#9fd0f2"/>
        <stop offset="0.55" stop-color="#2f7fcc"/>
        <stop offset="1" stop-color="var(--sea)"/>
      </linearGradient>
    </defs>
    <path class="corner-swoosh" d="M0,0 L285,0 C190,20 90,60 0,135 Z" fill="var(--blue)"/>
    <path class="corner-swoosh-gap" d="M0,0 L230,0 C150,22 70,55 0,108 Z" fill="var(--paper)"/>
    <path class="corner-swoosh-inner" d="M0,0 L175,0 C110,20 50,45 0,80 Z" fill="var(--blue)"/>

    <path class="wave-blue" d="M430,0 C465,95 520,205 605,285 C705,380 850,470 1024,538 L1024,0 Z" fill="var(--blue)"/>
    <path class="wave-black" d="M515,0 C555,110 615,215 700,275 C800,350 920,405 1024,432 L1024,0 Z" fill="var(--ink)"/>
    <path class="wave-blue-thin" d="M548,0 C585,100 635,180 710,230 C790,282 900,312 1024,318 L1024,0 Z" fill="var(--blue)"/>
    <path class="photo-yacht" role="img" aria-label="Photo of a white motor yacht cruising on blue open sea under a clear sky" d="M560,0 C595,95 640,160 712,208 C790,258 900,292 1024,298 L1024,0 Z" fill="url(#seaPhoto)"/>

    <path class="wave-bottom-blue" d="M300,1024 C450,945 610,845 790,815 C890,800 975,805 1024,812 L1024,1024 Z" fill="var(--blue)"/>
    <path class="wave-bottom-black" d="M365,1024 C505,940 632,860 792,835 C892,822 976,826 1024,830 L1024,1024 Z" fill="var(--ink)"/>
    <path class="wave-bottom-white" d="M388,1024 C528,943 650,866 796,843 C896,831 979,834 1024,838 L1024,1024 Z" fill="var(--white)"/>
    <path class="wave-bottom-front" d="M402,1024 C542,948 662,873 800,852 C900,840 981,843 1024,847 L1024,1024 Z" fill="var(--blue-deep)"/>
  </svg>

  <div class="brand">
    <span class="brand-name">Brinevale</span>
    <span class="brand-tagline">Yacht Management</span>
  </div>

  <h1 class="headline">
    <span class="headline-lead">Yacht Management</span>
    <span class="headline-line">Package also includes</span>
    <span class="headline-line">the following</span>
    <span class="headline-line headline-underline">Periodic services:</span>
  </h1>

  <ul class="services">
    <li class="service">Monthly full vessel systems<br>checklist inspections</li>
    <li class="service">Diver for hull cleaning and<br>inspection of props, shafts, and zincs</li>
    <li class="service">Interior/exterior detailing<br>and scheduled washdowns</li>
    <li class="service single">Manage haulout</li>
    <li class="service single">Pump-out services</li>
    <li class="service">On-call captain and<br>crew services</li>
  </ul>

  <p class="website">www.brinevaleyachts.com</p>

  <div class="contact">
    <span class="contact-call">
      <svg viewBox="0 0 32 32" aria-hidden="true">
        <circle cx="16" cy="16" r="14" fill="none" stroke="currentColor" stroke-width="2.5"/>
        <path d="M11.5 9.5c.6-.6 1.4-.5 1.8.1l1.5 2.3c.3.5.2 1.1-.2 1.5l-.9.8c.7 1.6 2 2.9 3.6 3.6l.8-.9c.4-.4 1-.5 1.5-.2l2.3 1.5c.6.4.7 1.2.1 1.8l-1 1c-.9.9-2.3 1.1-3.5.5-3-1.4-5.4-3.8-6.8-6.8-.6-1.2-.4-2.6.5-3.5z" fill="currentColor"/>
      </svg>
      Call now
    </span>
    <span class="contact-phone">1 (800) 555-0192</span>
  </div>
</main>
</body>
</html>
```